BrivoMatex. Lantern for the Steady Growth. Business card

Professional business card for BrivoMatex (Lantern for the Steady Growth)
My rationale: Strategy-> Execution-> Results-> Value that lead to the BrivoMatex name: We put the Lantern for the Steady Growth.
We deliver value to our customers helping them at defining a good strategy (cyan arrow). 90% of well formulated strategies fail due to poor execution so we also consider strategical execution very important (green arrow). Due to the execution we obtain the results (blue arrow). Finally, the results provide feedback to redefine strategy, and the new strategy has to be executed and new results obtained providing new feedback and on and on. It's like a wheel that finally, must create corporate value: value for shareholders, staholders, employees, providers...-

Target Market(s)

CEOs and steering comitees , invewrnent funds

Industry/Entity Type

Business Consultant

Contact Information for Business Card

Tommaso Ferlini
CEO & Founder
tommaso.ferlini@brivomatex.example
Mobile: +34 611.205.938
www.brivomatex.example

Colors

Designer to choose colors to be used in the design.

Requirements
Nice to have
• Nice to hace the words: Strategy, execution, results
• Nice to vave the claim: Lantern for the Steady Growth
• The three colors should be shown:
• cyan for STRATEGY
• green for EXECUTION
• blue for RESULTS
Should not have
• Complete black background

```html
<!DOCTYPE html>
<html lang="en">
<head>
<meta charset="utf-8">
<title>BrivoMatex – Business Card</title>
<link href="https://fonts.googleapis.com/css2?family=Open+Sans:wght@400;700&family=Questrial&display=swap" rel="stylesheet">
<style>
  :root {
    --backdrop: #3a3a3a;
    --card-white: #ffffff;
    --card-black: #0a0a0a;
    --map-tone: #161616;
    --brand-blue: #0b3a9e;
    --accent-cyan: #00aeef;
    --ink: #1a1a1a;
    --paper-ink: #f2f2f2;
  }
  * { margin: 0; padding: 0; box-sizing: border-box; }
  html, body { width: 1200px; height: 901px; overflow: hidden; }
  body {
    background: var(--backdrop);
    font-family: "Open Sans", Arial, sans-serif;
    position: relative;
  }
  .card {
    position: absolute;
    left: 250px;
    width: 700px;
    height: 400px;
    overflow: hidden;
    box-shadow: 0 10px 30px rgba(0,0,0,0.45);
  }
  /* Front side */
  .card-front { top: 34px; background: var(--card-white); }
  .front-brand {
    position: absolute;
    left: 60px;
    top: 150px;
    display: flex;
    align-items: center;
    gap: 12px;
  }
  .brand-dot {
    width: 18px; height: 18px; border-radius: 50%;
    background: var(--brand-blue);
  }
  .brand-name {
    font-family: "Open Sans", Arial, sans-serif;
    font-weight: 700;
    color: var(--brand-blue);
    font-size: 42px;
    letter-spacing: -0.5px;
    white-space: nowrap;
  }
  .front-divider {
    position: absolute;
    left: 385px;
    top: 105px;
    width: 2px;
    height: 130px;
    background: var(--accent-cyan);
  }
  .person {
    position: absolute;
    left: 420px;
    top: 110px;
  }
  .person-name {
    font-family: "Questrial", Arial, sans-serif;
    color: var(--accent-cyan);
    font-size: 27px;
    letter-spacing: 0.5px;
    line-height: 1;
    white-space: nowrap;
  }
  .person-title {
    font-size: 14px;
    color: var(--ink);
    margin-top: 4px;
  }
  .contact {
    position: absolute;
    left: 402px;
    top: 200px;
    list-style: none;
  }
  .contact li {
    display: flex;
    align-items: center;
    gap: 12px;
    font-size: 12px;
    color: var(--ink);
    letter-spacing: 0.3px;
    margin-bottom: 8px;
    white-space: nowrap;
  }
  .contact-icon { width: 16px; height: 16px; flex: none; }
  .front-footer { position: absolute; left: 0; bottom: 0; width: 700px; height: 40px; }
  .website {
    position: absolute;
    right: 24px;
    bottom: 10px;
    color: var(--paper-ink);
    font-size: 12px;
    letter-spacing: 6px;
    white-space: nowrap;
  }
  /* Back side */
  .card-back { top: 467px; background: var(--card-black); }
  .world-map {
    position: absolute;
    left: 60px; top: 30px;
    width: 580px; height: 320px;
    background: radial-gradient(ellipse at center, var(--map-tone) 0%, var(--card-black) 75%);
  }
  .back-brand {
    position: absolute;
    left: 0; right: 0;
    top: 160px;
    display: flex;
    justify-content: center;
    align-items: center;
    gap: 16px;
  }
  .back-brand .brand-name { font-size: 66px; }
  .back-brand .brand-dot { width: 26px; height: 26px; }
  .back-stripe {
    position: absolute;
    left: 0; bottom: 18px;
    width: 100%; height: 8px;
    background: var(--accent-cyan);
  }
</style>
</head>
<body>
  <section class="card card-front">
    <div class="front-brand">
      <span class="brand-dot"></span>
      <span class="brand-name">BrivoMatex</span>
    </div>
    <div class="front-divider"></div>
    <div class="person">
      <p class="person-name">Tommaso Ferlini</p>
      <p class="person-title">CEO &amp; Founder</p>
    </div>
    <ul class="contact">
      <li>
        <svg class="contact-icon" viewBox="0 0 16 16"><circle cx="8" cy="8" r="8" fill="var(--accent-cyan)"/><path d="M5.5 4.5l1.3 1.6-.8 1.1c.6 1.2 1.5 2.1 2.7 2.7l1.1-.8 1.6 1.3-.9 1.2c-2.8-.5-5-2.7-5.5-5.5z" fill="#fff"/></svg>
        +34 611.205.938
      </li>
      <li>
        <svg class="contact-icon" viewBox="0 0 16 16"><circle cx="8" cy="8" r="8" fill="var(--accent-cyan)"/><rect x="4" y="5.2" width="8" height="5.6" fill="none" stroke="#fff" stroke-width="1"/><path d="M4 5.4l4 3 4-3" fill="none" stroke="#fff" stroke-width="1"/></svg>
        tommaso.ferlini@brivomatex.example
      </li>
    </ul>
    <svg class="front-footer" viewBox="0 0 700 40" preserveAspectRatio="none">
      <polygon points="0,28 360,28 360,40 0,40" fill="var(--accent-cyan)"/>
      <polygon points="368,40 392,14 700,14 700,40" fill="var(--card-black)"/>
    </svg>
    <span class="website">www.brivomatex.example</span>
  </section>

  <section class="card card-back">
    <div class="world-map" role="img" aria-label="Faint world map in dark grey across the card back"></div>
    <div class="back-brand">
      <span class="brand-dot"></span>
      <span class="brand-name">BrivoMatex</span>
    </div>
    <div class="back-stripe"></div>
  </section>
</body>
</html>
```